Indoor Gun Range Web Design Project

Create a professional bold indoor gun range website. Logo colors are white, red, and black. This is a very professional gun range. Please use high quality stock images if possible. Stay away from a lot of militia type photos. Use your best judgement on what to put as a main image and headline.

Here are some websites that I like for design.

http://www.harborlinefirearms.example/
http://www.pagecrafthub.example/website-templates/51947.html
http://www.brightmarkworks.example/

Target Market(s)

Men ages 25-65

Industry/Entity Type

Gun

Requirements
Must have
• Bold lettering, logo attached, exciting photos.
Should not have
• A lot of militia photos.

```html
<!DOCTYPE html>
<html lang="en">
<head>
<meta charset="utf-8">
<title>True Mark Indoor Gun Range – The Range</title>
<link rel="stylesheet" href="https://fonts.googleapis.com/css2?family=Arimo:wght@400;700&display=swap">
<style>
  :root {
    --page-top: #f1f1f1;
    --page-mid: #e2e2e2;
    --page-bottom: #5e6061;
    --nav-bg: #2c2e2f;
    --nav-divider: #1b1c1d;
    --nav-text: #f2f2f2;
    --accent-red: #c8202a;
    --ink: #1e1e1e;
    --brand-ink: #2a2b2c;
    --frame-dark: #2a2b2c;
    --frame-edge: #3b3c3d;
    --button-top: #606263;
    --button-bottom: #3c3e3f;
    --panel-bg: #fbfcfc;
    --header-top: #5a5e5f;
    --header-bottom: #363a3b;
    --tab-bg: #2f3233;
    --tab-active: #4a4d4e;
    --footer-bg: #353738;
    --footer-line: #7b7d7e;
    --footer-text: #e6e6e6;
  }
  html, body { margin: 0; padding: 0; overflow: hidden; }
  body { width: 1200px; height: 925px; font-family: "Arimo", Arial, sans-serif; }
  .page {
    position: relative; width: 1200px; height: 925px; overflow: hidden;
    background: linear-gradient(to bottom, var(--page-top) 0%, var(--page-mid) 55%, #b9bbbc 78%, var(--page-bottom) 94%);
  }

  /* top navigation */
  .main-nav {
    position: absolute; top: 0; left: 434px; right: 0; height: 36px;
    background: linear-gradient(to bottom, #3a3c3d, var(--nav-bg));
    display: flex; box-shadow: 0 1px 3px rgba(0,0,0,.4);
  }
  .main-nav a {
    flex: 1 1 auto; display: flex; align-items: center; justify-content: center;
    color: var(--nav-text); text-decoration: none; font-size: 14.5px; font-weight: 700;
    border-left: 1px solid var(--nav-divider); box-shadow: inset 1px 0 0 #4a4c4d;
    padding: 0 14px; position: relative;
  }
  .main-nav a.is-active { background: #3f4243; }
  .main-nav a.is-active::after {
    content: ""; position: absolute; left: 0; right: 0; bottom: 0; height: 3px; background: var(--accent-red);
  }

  /* brand */
  .brand {
    position: absolute; left: 82px; top: 78px;
    font-size: 24px; font-weight: 400; line-height: 30px; color: var(--brand-ink);
    margin: 0;
  }

  /* hero */
  .hero {
    position: absolute; left: 77px; top: 143px; width: 1048px; height: 238px;
    background: linear-gradient(to bottom, var(--frame-edge), var(--frame-dark));
    border-radius: 3px; box-shadow: 0 10px 18px rgba(0,0,0,.35);
  }
  .hero-image {
    position: absolute; left: 17px; top: 16px; width: 767px; height: 200px;
    background: radial-gradient(ellipse at 35% 40%, #4a4a4a 0%, #1b1b1b 45%, #050505 100%);
    border: 1px solid #111;
  }
  .hero-links { position: absolute; left: 796px; top: 21px; width: 230px; }
  .hero-link {
    display: flex; align-items: center; justify-content: space-between;
    height: 61px; margin-bottom: 3px; padding: 0 18px 0 16px; box-sizing: border-box;
    background: linear-gradient(to bottom, var(--button-top), var(--button-bottom));
    color: #fff; font-size: 17.5px; font-weight: 700; text-decoration: none;
    text-shadow: 0 1px 1px rgba(0,0,0,.6); border-radius: 2px;
  }

  /* content panel */
  .content-panel {
    position: absolute; left: 77px; top: 418px; width: 1046px; height: 406px;
    background: var(--panel-bg); border-radius: 6px; box-shadow: 0 2px 6px rgba(0,0,0,.45);
  }
  .section-header {
    position: absolute; left: 5px; top: 5px; width: 1034px; height: 47px;
    background: linear-gradient(to bottom, var(--header-top), var(--header-bottom));
    border-radius: 3px 3px 0 0; border-bottom: 4px solid #7e8283;
  }
  .section-header h1 {
    margin: 0; padding-left: 20px; line-height: 47px; font-size: 20px; color: #fff;
    text-shadow: 0 1px 1px rgba(0,0,0,.6);
  }
  .section-tabs {
    position: absolute; left: 5px; top: 57px; width: 1034px; height: 35px;
    background: var(--tab-bg); display: flex; border-radius: 0 0 3px 3px;
  }
  .section-tabs a {
    color: #f0f0f0; text-decoration: none; font-size: 14px; font-weight: 700;
    padding: 0 16px; line-height: 35px; border-right: 1px solid #1d1f20;
  }
  .section-tabs a.is-active { background: var(--tab-active); }

  .section-body {
    position: absolute; left: 26px; top: 132px; width: 520px;
    font-size: 14px; line-height: 17px; color: var(--ink);
  }
  .section-body p { margin: 0 0 17px; }
  .section-photo {
    position: absolute; left: 592px; top: 133px; width: 420px; height: 206px;
    border: 1px solid #c8c8c8; background: #fff; padding: 4px; margin: 0;
  }
  .section-photo div {
    width: 100%; height: 100%;
    background: radial-gradient(ellipse at 45% 45%, #6b6252 0%, #2c2a27 45%, #0b0b0b 100%);
  }

  /* footer */
  .site-footer {
    position: absolute; left: 0; top: 870px; width: 1200px; height: 55px;
    background: var(--footer-bg); border-top: 6px solid var(--footer-line);
  }
  .site-footer p {
    margin: 0; position: absolute; right: 80px; top: 16px; color: var(--footer-text); font-size: 14px;
  }
</style>
</head>
<body>
<div class="page">

  <nav class="main-nav">
    <a href="#">Home</a>
    <a href="#" class="is-active">The Range</a>
    <a href="#">Range News</a>
    <a href="#">Specials</a>
    <a href="#">Membership</a>
    <a href="#">Reviews</a>
    <a href="#">About</a>
    <a href="#">Contact</a>
  </nav>

  <p class="brand">True Mark Indoor Gun Range</p>

  <section class="hero">
    <div class="hero-image" role="img" aria-label="Close-up of a silver pistol with hollow-point rounds on a black surface"></div>
    <div class="hero-links">
      <a class="hero-link" href="#">Shooting Range
        <svg width="36" height="36" viewBox="0 0 36 36" aria-hidden="true">
          <g fill="none" stroke="#2b2d2e" stroke-width="2">
            <circle cx="18" cy="18" r="13"/><circle cx="18" cy="18" r="7"/>
            <path d="M18 1v10M18 25v10M1 18h10M25 18h10"/>
          </g>
          <circle cx="18" cy="18" r="2.5" fill="#2b2d2e"/>
        </svg>
      </a>
      <a class="hero-link" href="#">Specials</a>
      <a class="hero-link" href="#">Join Today!</a>
    </div>
  </section>

  <main class="content-panel">
    <div class="section-header"><h1>The Range</h1></div>
    <nav class="section-tabs">
      <a href="#" class="is-active">The Range</a>
      <a href="#">Firearms</a>
      <a href="#">Training</a>
      <a href="#">Fees</a>
      <a href="#">News</a>
      <a href="#">Rules</a>
    </nav>
    <div class="section-body">
      <p><strong>True Mark</strong>’s Indoor Range sed ut perspiciatis unde omnis iste natus error settle voluptatem accusantium doloremque laudantium, totam rem aperiam, eaque ipsas quae ab illo inventore veritatis et quasi architecto beatae vitae dicta sunt explicabo. Nemo enim ipsam voluptatem.</p>
      <p>Voluptas sit aspernatur aut odit aut fugit, sed quia consequuntur magni dolores eos quiratione voluptatem sequi nesciunt. Neque porro quisquam est, qui dolorem ipse quia dolor sit amet, consectetur, adipisci velit, sed quia non numquam eius modi to mpora incidunt ut labore et dolore magnam aliquam quaerat voluptatem. Ut enimt ad minima veniam, quis nostrum exercitationem ullam corporis suscipit laboriosam, nisi ut aliquid ex ea commodi consequatur? Quis autem vel eum iure reprehenderit qui in ea voluptate velit esse quam nihil molestiae consequatur vel illum to dolorem eum fugiat quo voluptas nulla pariatur.</p>
    </div>
    <figure class="section-photo">
      <div role="img" aria-label="Shooter in safety glasses aiming a revolver against a dark background"></div>
    </figure>
  </main>

  <footer class="site-footer">
    <p>© 2012&nbsp; True Mark Indoor Gun Range</p>
  </footer>

</div>
</body>
</html>
```